Business Card Design for Pastor/Church Leadership - simple, elegant, "different"

Design a name card based on logo and color from our branding guide - see file "BWF Logo and Color".
The teal frame around the logo is not part of the logo and is a not necessary design element for the name card (as the attached PDF file may suggest).
The font suggested by branding is "Frutiger 55 Roman".
The file "not good.pdf", a sample of a name card that is NOT good.
- fonts too small to read
- the tagline on the logo "Still waters, bright path" not easy to read with logo used in this design
- "MAPLE GROVE CHAPEL" unnecessarily duplicated - possibly because logo too small
- not sure about the green frame, probably better to drop

Target Market(s)

broad, all people the pastor of an international church in Tokyo meets

Industry/Entity Type

Business

Contact Information for Business Card

Everett L. Pranzoni
Pastor
3-9-4 Kamiyacho, Shibuya-ku
Tokyo 150-0082 (Church)
2-18 Sarugakucho, Shibuya-ku
Tokyo 150-0046 (Home)
Tel: 03-5712-0368
E-mail: pastor@maplegrovechapel.org
URL: http://www.maplegrovechapel.org

Font styles to use
Sans Serif
Other font styles liked:
• Frutiger 55 Roman (want, not must)

Requirements
Must have
• must include logo
• must make use of the "bright turquoise color"
• Cyan = 59, Magenta = 0, Yellow=24, Black=0
• Red=3.1%, Green=91%, Blue=87.1%
• Key Info (name) must be easy to read (see notes on bad sample namecard attached)

```html
<!DOCTYPE html>
<html lang="en">
<head>
<meta charset="utf-8">
<title>Maple Grove Chapel – Business Card</title>
<link rel="stylesheet" href="https://fonts.googleapis.com/css2?family=Source+Sans+3:ital,wght@0,400;0,600;1,400&display=swap">
<style>
  :root {
    --page-bg: #ececec;
    --card-white: #ffffff;
    --brand-teal: #69c8c8;
    --logo-teal: #4dbfbe;
    --ink-dark: #33413f;
    --ink-light: #ffffff;
  }
  * { margin: 0; padding: 0; box-sizing: border-box; }
  html, body {
    width: 1200px; height: 840px; overflow: hidden;
    background: var(--page-bg);
    font-family: "Source Sans 3", sans-serif;
  }
  .business-card {
    position: absolute; left: 75px; top: 120px;
    width: 1050px; height: 600px;
    background: var(--card-white);
    overflow: hidden;
  }
  .teal-panel { position: absolute; inset: 0; width: 100%; height: 100%; }
  .teal-panel path { fill: var(--brand-teal); }

  .identity {
    position: absolute; left: 90px; top: 190px; width: 330px;
    color: var(--logo-teal); text-align: left;
  }
  .identity-mark {
    display: flex; align-items: center; gap: 16px;
    font-size: 72px; font-weight: 600; line-height: 1;
    margin-left: 60px;
  }
  .identity-mark .mark-square {
    width: 30px; height: 30px; background: var(--logo-teal);
  }
  .church-name {
    margin-top: 70px;
    font-size: 34px; font-weight: 400; letter-spacing: 0.2px;
    padding-bottom: 6px;
    border-bottom: 2px solid var(--logo-teal);
    white-space: nowrap;
  }
  .church-tagline {
    margin-top: 8px; padding-left: 48px;
    font-size: 26px; white-space: nowrap;
  }

  .contact-block {
    position: absolute; right: 60px; top: 50px;
    text-align: right; color: var(--ink-dark);
  }
  .person-name { font-size: 46px; font-weight: 600; line-height: 1.05; }
  .person-role {
    font-size: 34px; font-style: italic; color: var(--ink-light);
    line-height: 1.1;
  }
  .contact-lines { margin-top: 26px; font-size: 23px; line-height: 1.3; color: var(--ink-light); }
  .address { margin-top: 34px; font-size: 23px; line-height: 1.45; }
</style>
</head>
<body>
  <div class="business-card">
    <svg class="teal-panel" viewBox="0 0 1050 600" preserveAspectRatio="none" aria-hidden="true">
      <path d="M420,0 H1050 V560 H770 Q540,560 490,330 L425,0 Z"/>
    </svg>

    <div class="identity">
      <div class="identity-mark"><span class="mark-square"></span>BWF</div>
      <div class="church-name">MAPLE GROVE CHAPEL</div>
      <div class="church-tagline">Still waters, bright path</div>
    </div>

    <div class="contact-block">
      <div class="person-name">Everett L. Pranzoni</div>
      <div class="person-role">Pastor</div>
      <div class="contact-lines">
        03-5712-0368<br>
        pastor@maplegrovechapel.org<br>
        www.maplegrovechapel.org
      </div>
      <div class="address">
        3-9-4 Kamiyacho, Shibuya-ku<br>
        Tokyo 150-0082 (Church)
      </div>
      <div class="address">
        2-18 Sarugakucho, Shibuya-ku<br>
        Tokyo 150-0046 (Home)
      </div>
    </div>
  </div>
</body>
</html>
```